Iconic Australian Wine Brand looking for a complete brand makeover

- Require a new label design for the Clover Ridge range of wines
- Complete brand makeover with refreshed packaging design
- Inspiration for consumers to see the brand in a new light
- The final design should communicate fun, energetic and modern packaging with the aim of engaging our core target market of 20 - 35 year old female wine drinkers, while re-engaging our loyal female demographic of 35+ year olds.

Target Market(s)

Engage a Core target market of 20-35 year old female wine drinkers / secondary target market: re-engage our loyal female demographic of 35+ year olds

Requirements
Must have
• Complete brand makeover in order to re-engage our loyal female drinkers, now in their mid to late 30's
Nice to have
• Play on words for the Brand name

```html
<!DOCTYPE html>
<html lang="en">
<head>
<meta charset="utf-8">
<title>Clover Ridge – Wine Label</title>
<link href="https://fonts.googleapis.com/css2?family=Kalam:wght@400&display=swap" rel="stylesheet">
<style>
  :root {
    --cream: #fcf8d6;
    --border-pink: #c8205a;
    --figure-pink: #d21a5c;
    --ink: #3a3a3c;
  }
  html, body {
    margin: 0;
    padding: 0;
    width: 1200px;
    height: 1106px;
    overflow: hidden;
    background: var(--cream);
  }
  .canvas {
    position: relative;
    width: 1200px;
    height: 1106px;
    background: var(--cream);
  }
  .label {
    position: absolute;
    left: 333px;
    top: 73px;
    width: 533px;
    height: 960px;
    box-sizing: border-box;
    border: 2px solid var(--border-pink);
    border-radius: 8px;
    background: var(--cream);
  }
  .brand-name {
    position: absolute;
    left: 200px;
    top: 500px;
    margin: 0;
    width: 760px;
    transform: translate(-50%, -50%) rotate(-90deg);
    text-align: center;
    white-space: nowrap;
    font-family: "Kalam", cursive;
    font-weight: 400;
    font-size: 140px;
    line-height: 1;
    color: var(--ink);
  }
  .sisters-figures {
    position: absolute;
    left: 298px;
    top: 653px;
    width: 133px;
    height: 230px;
    border-radius: 30px 30px 6px 6px;
    background: linear-gradient(180deg, #d82466 0%, var(--figure-pink) 100%);
  }
</style>
</head>
<body>
  <main class="canvas">
    <section class="label">
      <h1 class="brand-name">Clover Ridge</h1>
      <div class="sisters-figures" role="img" aria-label="Illustration of four standing female silhouettes in pink"></div>
    </section>
  </main>
</body>
</html>
```